Business Card Design

We need a business card design for a consulting firm which provides safety and risk management consulting services for public venues, hotels and tourist attractions. The business card design should include the attached logo unedited with a design based on incorporating the existing logo with a design of geometric patterns or lines on a predominantly white background.

Industry/Entity Type

Business

Contact Information for Business Card

Dane Morravik
Director & Principal Consultant

Ph: +61 (0) 478506 214
PO Box 456 Brenmoor Vale, NSW Australia 2611
info@corvalrisksafety.example

(back of card to include website www.corvalrisksafety.example

```html
<!DOCTYPE html>
<html lang="en">
<head>
<meta charset="utf-8">
<title>Corval Risk &amp; Safety — Business Cards</title>
<link rel="stylesheet" href="https://fonts.googleapis.com/css2?family=Open+Sans:wght@400;600;700&display=swap">
<style>
  :root {
    --page-bg: #ece9e4;
    --brand-blue: #2199d6;
    --ink-blue: #1e8fd0;
    --card-white: #ffffff;
    --text-grey: #4a4a4a;
    --text-dark: #333333;
    --icon-blue: #2a8fd4;
    --shadow: rgba(0, 0, 0, 0.22);
  }
  * { box-sizing: border-box; margin: 0; padding: 0; }
  html, body {
    width: 1200px;
    height: 900px;
    overflow: hidden;
    background: var(--page-bg);
    font-family: "Open Sans", Arial, sans-serif;
  }
  .canvas {
    position: relative;
    width: 1200px;
    height: 900px;
  }
  .card {
    position: absolute;
    width: 620px;
    height: 354px;
    border-radius: 14px;
    box-shadow: 0 12px 30px var(--shadow);
    overflow: hidden;
  }

  /* Back of card */
  .card--back {
    left: 110px;
    top: 60px;
    background: var(--brand-blue);
    color: var(--card-white);
  }
  .card--back .brand {
    position: absolute;
    left: 70px;
    top: 118px;
    display: flex;
    align-items: center;
    gap: 16px;
  }
  .brand-dot {
    width: 34px;
    height: 34px;
    border-radius: 50%;
    flex: none;
  }
  .card--back .brand-dot { background: var(--card-white); }
  .card--back .brand-name {
    font-size: 34px;
    font-weight: 700;
    letter-spacing: 1px;
    color: var(--card-white);
  }
  .card--back .website {
    position: absolute;
    left: 140px;
    top: 226px;
    font-size: 22px;
    font-weight: 400;
    letter-spacing: 0.3px;
  }

  /* Front of card */
  .card--front {
    left: 470px;
    top: 476px;
    background: var(--card-white);
    color: var(--text-grey);
  }
  .card--front .brand {
    position: absolute;
    left: 40px;
    top: 34px;
    display: flex;
    align-items: center;
    gap: 12px;
  }
  .card--front .brand-dot {
    width: 26px;
    height: 26px;
    background: var(--ink-blue);
  }
  .card--front .brand-name {
    font-size: 27px;
    font-weight: 700;
    letter-spacing: 0.8px;
    color: var(--ink-blue);
  }
  .address {
    position: absolute;
    left: 56px;
    top: 122px;
    font-size: 17px;
    line-height: 1.3;
    color: var(--text-grey);
  }
  .contact-list {
    position: absolute;
    left: 56px;
    top: 192px;
    list-style: none;
  }
  .contact-list li {
    display: flex;
    align-items: center;
    gap: 10px;
    font-size: 16px;
    color: var(--text-dark);
    margin-bottom: 12px;
  }
  .contact-list svg { width: 14px; height: 14px; flex: none; }
  .person {
    position: absolute;
    right: 46px;
    top: 160px;
    text-align: right;
  }
  .person-name {
    font-size: 24px;
    font-weight: 700;
    color: var(--ink-blue);
    letter-spacing: 0.3px;
  }
  .person-title {
    font-size: 15px;
    font-weight: 400;
    color: var(--text-dark);
    margin-top: 2px;
  }
</style>
</head>
<body>
<main class="canvas">

  <section class="card card--back" aria-label="Back of business card">
    <div class="brand">
      <span class="brand-dot"></span>
      <span class="brand-name">CORVAL RISK &amp; SAFETY</span>
    </div>
    <p class="website">www.corvalrisksafety.example</p>
  </section>

  <section class="card card--front" aria-label="Front of business card">
    <div class="brand">
      <span class="brand-dot"></span>
      <span class="brand-name">CORVAL RISK &amp; SAFETY</span>
    </div>

    <p class="address">PO Box 456 Brenmoor Vale,<br>NSW Australia 2611</p>

    <ul class="contact-list">
      <li>
        <svg viewBox="0 0 16 16" aria-hidden="true"><path fill="var(--icon-blue)" d="M4 1.5l2.2 3-1.3 1.6c.8 1.9 2.4 3.5 4.3 4.3l1.6-1.3 3 2.2-1.2 2.4C7 13.4 2.6 9 2.1 2.7z"/></svg>
        +61 (0) 478506 214
      </li>
      <li>
        <svg viewBox="0 0 16 16" aria-hidden="true"><rect x="1" y="3" width="14" height="10" fill="var(--icon-blue)"/><path d="M1 3.5l7 5 7-5" fill="none" stroke="#fff" stroke-width="1.2"/></svg>
        info@corvalrisksafety.example
      </li>
      <li>
        <svg viewBox="0 0 16 16" aria-hidden="true"><circle cx="8" cy="8" r="6.5" fill="none" stroke="var(--icon-blue)" stroke-width="1.4"/><ellipse cx="8" cy="8" rx="2.8" ry="6.5" fill="none" stroke="var(--icon-blue)" stroke-width="1.2"/><path d="M1.5 8h13" stroke="var(--icon-blue)" stroke-width="1.2"/></svg>
        www.corvalrisksafety.example
      </li>
    </ul>

    <div class="person">
      <p class="person-name">Dane Morravik</p>
      <p class="person-title">Director &amp; Principal Consultant</p>
    </div>
  </section>

</main>
</body>
</html>
```